Red Sea Boat trips in need of Business Card for Private Boat Tours

We need a Business card for a new business set-up in Egypt on the Red Sea for private snorkelling and boat excursions to one of the world's most beautiful reefs. We have wording logo already set-up which matches the boat but we need business cards to be bright and colourful with pictures of boat

Industry/Entity Type

Tourism

Contact Information for Business Card

Two Silver Herons (font provided) Boat Trips

```html
<!DOCTYPE html>
<html lang="en">
<head>
<meta charset="utf-8">
<title>Two Silver Herons – Business Card</title>
<link href="https://fonts.googleapis.com/css2?family=Jost:wght@400;500;600&display=swap" rel="stylesheet">
<style>
  :root {
    --bg: #e9e4dc;
    --reef-deep: #2a5553;
    --reef-mid: #3f989c;
    --reef-light: #8fd0cd;
    --sand: #cfe9e4;
    --coral: #8a7a4c;
    --ink-blue: #2b2f8f;
    --ink-dark: #22253a;
    --mark: #111318;
    --front-mark: #e6f6fb;
  }
  * { box-sizing: border-box; margin: 0; padding: 0; }
  html, body { width: 1200px; height: 900px; overflow: hidden; }
  body {
    background: var(--bg);
    font-family: "Jost", sans-serif;
    display: flex;
    flex-direction: column;
    align-items: center;
    justify-content: center;
    gap: 36px;
  }
  .card {
    position: relative;
    width: 700px;
    height: 400px;
    border-radius: 30px;
    overflow: hidden;
    box-shadow: 0 10px 24px rgba(0,0,0,.25);
  }
  .card__photo { position: absolute; inset: 0; }
  .card--front .card__photo {
    background:
      radial-gradient(ellipse 40% 30% at 62% 30%, var(--sand) 0%, transparent 70%),
      linear-gradient(180deg, transparent 50%, rgba(20,60,62,.55) 100%),
      linear-gradient(135deg, var(--reef-deep) 0%, var(--reef-mid) 45%, var(--reef-light) 65%, var(--reef-deep) 100%);
  }
  .card--back .card__photo {
    background:
      linear-gradient(160deg, #b9c8d2 0%, #7fc6c9 30%, #3c9aa3 50%, transparent 60%),
      linear-gradient(200deg, transparent 40%, var(--coral) 70%, #3a3f3c 100%),
      #3a7f86;
  }
  .front__mark {
    position: absolute;
    left: 50%; top: 72%;
    transform: translate(-50%, -50%);
    font-size: 52px;
    font-weight: 600;
    color: var(--front-mark);
    white-space: nowrap;
  }
  .contact {
    position: absolute;
    left: 40px; top: 44px;
    color: var(--ink-dark);
    font-size: 18px;
    line-height: 1.25;
  }
  .contact__name { color: var(--ink-blue); font-weight: 600; font-size: 26px; letter-spacing: .5px; }
  .contact__role { margin-bottom: 12px; }
  .contact__address { margin-bottom: 8px; }
  .contact__line { display: flex; align-items: center; gap: 10px; margin-top: 4px; }
  .contact__line svg { width: 18px; height: 18px; fill: var(--ink-blue); flex: none; }
  .back__mark {
    position: absolute;
    right: 30px; bottom: 30px;
    font-size: 44px;
    font-weight: 600;
    color: var(--mark);
    white-space: nowrap;
  }
</style>
</head>
<body>
  <section class="card card--front">
    <div class="card__photo" role="img" aria-label="Underwater photo of a snorkeller diving over a sandy reef floor surrounded by coral"></div>
    <div class="front__mark">Two Silver Herons</div>
  </section>

  <section class="card card--back">
    <div class="card__photo" role="img" aria-label="Underwater photo of a colourful coral reef with tropical fish in clear turquoise water"></div>
    <div class="contact">
      <div class="contact__name">JOHN SMITH</div>
      <div class="contact__role">Director</div>
      <div class="contact__address">00 dummy city<br>dummy place 0000</div>
      <div class="contact__line">
        <svg viewBox="0 0 24 24" aria-hidden="true"><path d="M6.6 10.8a15 15 0 0 0 6.6 6.6l2.2-2.2a1 1 0 0 1 1-.25 11.4 11.4 0 0 0 3.6.57 1 1 0 0 1 1 1V20a1 1 0 0 1-1 1A17 17 0 0 1 3 4a1 1 0 0 1 1-1h3.5a1 1 0 0 1 1 1c0 1.25.2 2.45.57 3.6a1 1 0 0 1-.25 1z"/></svg>
        <span>300-200-9000</span>
      </div>
      <div class="contact__line">
        <svg viewBox="0 0 24 24" aria-hidden="true"><path d="M2 5h20v14H2z M2 5l10 8 10-8" fill="none" stroke="#2b2f8f" stroke-width="2"/></svg>
        <span>info@twosilverherons.com</span>
      </div>
      <div class="contact__line">
        <svg viewBox="0 0 24 24" aria-hidden="true"><g fill="none" stroke="#2b2f8f" stroke-width="1.8"><circle cx="12" cy="12" r="9"/><ellipse cx="12" cy="12" rx="4" ry="9"/><path d="M3 12h18M5 7h14M5 17h14"/></g></svg>
        <span>www.twosilverherons.com</span>
      </div>
    </div>
    <div class="back__mark">Two Silver Herons</div>
  </section>
</body>
</html>
```